Crestline Gas and Plumbing Business Card Design

I am after a business card design for my plumbing business called 'Crestline Gas & Plumbing'. I do all types of plumbing and gas work and specialise in general maintenance plumbing. Would like to see designs using current logo

Industry/Entity Type

Plumbing

Contact Information for Business Card

Name - Dale Whitcombe
Phone number - 0455163027
Email - admin@crestlinegasandplumbing.example.com.au
ABN - 68204915336

```html
<!DOCTYPE html>
<html lang="en">
<head>
<meta charset="utf-8">
<title>Crestline Gas &amp; Plumbing — Business Card</title>
<link rel="stylesheet" href="https://fonts.googleapis.com/css2?family=Exo+2:wght@500;600;700&family=Roboto:wght@400&display=swap">
<style>
  :root {
    --backdrop: #1f1f1f;
    --blue-deep: #27409c;
    --blue-mid: #1471c0;
    --white: #ffffff;
    --brand-blue: #1d4fa8;
  }
  * { box-sizing: border-box; margin: 0; padding: 0; }
  html, body {
    width: 1125px;
    height: 1200px;
    overflow: hidden;
    background: var(--backdrop);
  }
  .card {
    position: absolute;
    left: 171px;
    width: 800px;
    height: 456px;
    transform: scale(1.0325);
    transform-origin: top left;
    overflow: hidden;
    font-family: "Exo 2", sans-serif;
  }
  .card--front { top: 106px; background: var(--white); }
  .card--back {
    top: 639px;
    background: radial-gradient(ellipse at 50% 40%, var(--blue-mid) 0%, var(--blue-deep) 75%);
  }
  .front-band {
    position: absolute;
    left: 0; top: 0;
    width: 800px;
    height: 236px;
    background: radial-gradient(ellipse at 55% 10%, var(--blue-mid) 0%, var(--blue-deep) 85%);
  }
  .contact {
    position: absolute;
    right: 44px;
    top: 46px;
    text-align: right;
    color: var(--white);
  }
  .contact__name { font-size: 26px; font-weight: 600; margin-bottom: 14px; }
  .contact__row {
    display: flex;
    justify-content: flex-end;
    align-items: center;
    gap: 10px;
    font-size: 15px;
    font-weight: 600;
    height: 25px;
  }
  .contact__row svg { width: 17px; height: 17px; flex: none; }
  .contact__abn { font-size: 16px; font-weight: 600; margin-top: 7px; margin-right: 1px; }
  .brand {
    position: absolute;
    left: 62px;
    top: 318px;
    display: flex;
    align-items: center;
    gap: 12px;
    color: var(--brand-blue);
    font-size: 25px;
    font-weight: 700;
  }
  .brand__dot { width: 34px; height: 34px; border-radius: 50%; background: var(--brand-blue); }
  .back-brand {
    position: absolute;
    left: 0; right: 0;
    top: 150px;
    display: flex;
    flex-direction: column;
    align-items: center;
    gap: 22px;
    color: var(--white);
    font-size: 30px;
    font-weight: 700;
  }
  .back-brand__dot { width: 90px; height: 90px; border-radius: 50%; background: var(--white); }
  .back-url {
    position: absolute;
    left: 0; right: 0;
    top: 393px;
    text-align: center;
    color: var(--white);
    font-family: "Roboto", sans-serif;
    font-size: 17px;
    letter-spacing: 3.6px;
  }
</style>
</head>
<body>
  <section class="card card--front">
    <div class="front-band" role="img" aria-label="Decorative blue wave with an orange and yellow ribbon across the top of the card"></div>

    <div class="contact">
      <p class="contact__name">Dale Whitcombe</p>
      <p class="contact__row">0455163027
        <svg viewBox="0 0 24 24" aria-hidden="true"><path fill="#fff" d="M6.6 10.8a15 15 0 0 0 6.6 6.6l2.2-2.2a1 1 0 0 1 1-.25 11.4 11.4 0 0 0 3.6.57 1 1 0 0 1 1 1V20a1 1 0 0 1-1 1A17 17 0 0 1 3 4a1 1 0 0 1 1-1h3.5a1 1 0 0 1 1 1c0 1.25.2 2.45.57 3.57a1 1 0 0 1-.25 1z"/></svg>
      </p>
      <p class="contact__row">admin@crestlinegasandplumbing.example.com.au
        <svg viewBox="0 0 24 24" aria-hidden="true"><rect x="2" y="5" width="20" height="14" fill="#fff"/><path d="M2 5l10 8 10-8" fill="none" stroke="#1d55b0" stroke-width="1.6"/></svg>
      </p>
      <p class="contact__row">crestlinegasandplumbing.example.com.au
        <svg viewBox="0 0 24 24" aria-hidden="true"><circle cx="12" cy="12" r="10" fill="#fff"/><path d="M8 6c2 1 3 3 1 5s1 4 3 4M15 5c-1 2 1 3 3 3M14 19c1-2 3-2 4-3" fill="none" stroke="#1d55b0" stroke-width="1.8"/></svg>
      </p>
      <p class="contact__abn">ABN - 68204915336</p>
    </div>

    <div class="brand">
      <span class="brand__dot"></span>
      <span class="brand__name">Crestline Gas &amp; Plumbing</span>
    </div>
  </section>

  <section class="card card--back">
    <div class="back-brand">
      <span class="back-brand__dot"></span>
      <span class="back-brand__name">Crestline Gas &amp; Plumbing</span>
    </div>
    <p class="back-url">www.crestlinegasandplumbing.example.com.au</p>
  </section>
</body>
</html>
```